International oil and gas consultancy needs a business card design

We need a business card design for a new oil and gas consultancy business based in Perth Australia. This is a professional services business and needs a moderately conservative type of business card. The business card also needs to be simple and uncluttered. The colour of the business logo is dark red (see attached file).
The front of the card should have a white background and mainly black lettering and perhaps some use of dark red and/or grey (your choice).
The back of the card should have a light grey background with dark red, black and or both dark red & black lettering (your choice).
Please find attached a clear brief of how I would like the business card designed.
Updates

Hello Everyone, I have slightly modified the brief. The main change is to incorporate some dark red and grey colours into the card, while still keeping the black lettering dominant. I have made the changes in the attached detailed brief document. Regards

Please note, the front of the card must say Harbor Ledger Advisory (in addition to the logo).

Industry/Entity Type

Conservative

Requirements
Must have
• brief has been updated. please refer to attachment for details.

Front of the card MUST say Harbor Ledger Advisory (in addition to the logo)

```html
<!DOCTYPE html>
<html lang="en">
<head>
<meta charset="utf-8">
<title>Harbor Ledger Advisory – Business Card</title>
<link rel="stylesheet" href="https://fonts.googleapis.com/css2?family=Exo+2:wght@400;600;700&display=swap">
<style>
  :root {
    --bg: #2a2a2c;
    --card-light: #f4f4f4;
    --card-mid: #d9d9d9;
    --brand-red: #8e1b1d;
    --ink: #2b2b2b;
    --ink-soft: #555555;
    --white: #ffffff;
  }
  * { box-sizing: border-box; margin: 0; padding: 0; }
  html, body { width: 1200px; height: 870px; overflow: hidden; }
  body {
    background: var(--bg);
    font-family: "Exo 2", sans-serif;
    display: flex;
    flex-direction: column;
    align-items: center;
    justify-content: center;
    gap: 40px;
  }
  .card {
    position: relative;
    width: 640px;
    height: 366px;
    overflow: hidden;
    box-shadow: 0 10px 30px rgba(0,0,0,0.45);
  }
  .card--back {
    background: radial-gradient(ellipse at 60% 40%, var(--white) 0%, var(--card-light) 45%, var(--card-mid) 100%);
    display: flex;
    align-items: center;
    justify-content: center;
  }
  .brand-name {
    display: flex;
    align-items: center;
    gap: 12px;
    color: var(--brand-red);
    font-weight: 700;
    letter-spacing: 0.5px;
    line-height: 1;
  }
  .brand-name__square {
    width: 18px;
    height: 18px;
    background: var(--brand-red);
    flex: none;
  }
  .card--back .brand-name { font-size: 38px; }

  .card--front { background: var(--card-light); }
  .card--front .upper {
    position: absolute;
    inset: 0 0 42% 0;
    background: radial-gradient(ellipse at 70% 60%, var(--white) 0%, var(--card-light) 50%, var(--card-mid) 100%);
  }
  .contact-list {
    position: absolute;
    top: 22px;
    left: 30px;
    list-style: none;
    display: flex;
    flex-direction: column;
    gap: 8px;
    color: var(--ink);
    font-size: 13.5px;
  }
  .contact-list li { display: flex; align-items: center; gap: 10px; }
  .contact-list svg { width: 13px; height: 13px; fill: var(--ink-soft); flex: none; }
  .card--front .brand-name {
    position: absolute;
    right: 30px;
    top: 112px;
    font-size: 26px;
  }
  .band {
    position: absolute;
    left: 0; right: 0; bottom: 0;
    height: 42%;
    background: var(--brand-red);
    color: var(--white);
  }
  .address {
    position: absolute;
    top: 20px;
    left: 30px;
    font-size: 17px;
    line-height: 1.35;
    letter-spacing: 0.3px;
  }
  .person {
    position: absolute;
    right: 30px;
    bottom: 22px;
    text-align: right;
  }
  .person__name { font-size: 19px; font-weight: 600; letter-spacing: 0.8px; text-transform: uppercase; }
  .person__title { font-size: 15px; letter-spacing: 0.4px; }
</style>
</head>
<body>

  <section class="card card--back" aria-label="Card back">
    <div class="brand-name"><span class="brand-name__square"></span>Harbor Ledger Advisory</div>
  </section>

  <section class="card card--front" aria-label="Card front">
    <div class="upper"></div>
    <ul class="contact-list">
      <li><svg viewBox="0 0 16 16"><path d="M3 1l3 3-2 2c1 2 3 4 5 5l2-2 3 3-2 3C6 15 1 10 1 3z"/></svg>041 228 5093</li>
      <li><svg viewBox="0 0 16 16"><path d="M4 0h8v16H4zM5.5 2v10h5V2z"/></svg>041 228 5093</li>
      <li><svg viewBox="0 0 16 16"><path d="M2 5h12v9H2zM4 1h7v4H4zM4 8h3v1H4zm5 0h3v1H9zM4 11h3v1H4zm5 0h3v1H9z"/></svg>041 228 5093</li>
      <li><svg viewBox="0 0 16 16"><path d="M1 3h14v10H1zM2.5 4.5L8 9l5.5-4.5" stroke="#f4f4f4" stroke-width="1"/></svg>m.greaves@harborledger.com</li>
      <li><svg viewBox="0 0 16 16"><path d="M8 1a7 7 0 100 14A7 7 0 008 1zm0 1.5c1 1.2 1.6 3 1.7 4.8H6.3C6.4 5.5 7 3.7 8 2.5zM2.6 8.7h2.3c.1 1.7.6 3.3 1.4 4.6A5.6 5.6 0 012.6 8.7zm0-1.4a5.6 5.6 0 013.7-4.6C5.5 4 5 5.6 4.9 7.3zm3.7 1.4h3.4c-.1 1.8-.7 3.6-1.7 4.8-1-1.2-1.6-3-1.7-4.8zm4.8 0h2.3a5.6 5.6 0 01-3.7 4.6c.8-1.3 1.3-2.9 1.4-4.6zm0-1.4c-.1-1.7-.6-3.3-1.4-4.6a5.6 5.6 0 013.7 4.6z"/></svg>www.harborledger.com</li>
    </ul>
    <div class="brand-name"><span class="brand-name__square"></span>Harbor Ledger Advisory</div>
    <div class="band">
      <p class="address">Level 18, 240 Terrace Road<br>Perth WA</p>
      <div class="person">
        <p class="person__name">Martin Greaves</p>
        <p class="person__title">Managing Director</p>
      </div>
    </div>
  </section>

</body>
</html>
```